Business card design for Velvet Harbor

We need business cards designed for our new marketing consulting company, Velvet Harbor. Our services include marketing strategy, go-to-market and launch planning, growth strategy, and execution. We serve medical technology and health technology companies, from startups to well-established growth companies.

The business cards should feel professional, credible, reliable and trustworthy, and should instill confidence. Also bold, creative, and modern.

The design must use the Velvet Harbor logo.

The primary brand color is this orange: #FF5501
A secondary color that you can use is this gray: #282B2D
I would prefer only to use the orange and gray. But if you feel you really need an additional accent color (please use it very sparingly, as little as possible), you can use this blue for small accent purposes: #009FED

Attached are the logo files. The main logo is the one with a little bit of orange on the left and the rest is gray.

The business card should include the following:

Velvet Harbor logo
First name and last name
Title
Email address
Phone number and type (in whatever order looks best for the design
Website (the website does not need to be in the same block as the personal info)

For example:

Nessa Pryle
Founder & Principal
nessa@velvetharbor.com
+1.628.309.4156 mobile (can use "." or spaces in between blocks of numbers)
velvetharbor.com (somewhere on the card, it does not need to be with the personal info; and note that there is no "www." at the beginning)

Note that there will be no address listed on the business card.

Target Market(s)

Executives (CEO, head of marketing, head of sales) at medical technology and health technology companies, mostly in their 40s and older, well-educated, often with advanced degrees. They are strategic thinkers, responsible for budgets, and familiar with P&L. Their comfort with and trust in using outside consultants varies.

Industry/Entity Type

Medical technology and health technology companies.

Contact Information for Business Card

See project description

Font styles to use
Sans Serif

Requirements
Must have
• Logo and see Business card details section above.

```html
<!DOCTYPE html>
<html lang="en">
<head>
<meta charset="utf-8">
<title>Velvet Harbor — Business Card</title>
<link href="https://fonts.googleapis.com/css2?family=Arimo:wght@400;700&display=swap" rel="stylesheet">
<style>
  :root {
    --stage: #e9e4dc;
    --card: #1f1f1f;
    --ink: #ffffff;
    --orange: #ff5501;
    --orange-deep: #d55f1e;
    --shadow: rgba(0,0,0,0.28);
  }
  * { margin: 0; padding: 0; box-sizing: border-box; }
  html, body { width: 1200px; height: 675px; overflow: hidden; }
  body {
    background: var(--stage);
    font-family: "Arimo", Arial, sans-serif;
    position: relative;
  }
  .card {
    position: absolute;
    top: 187px;
    width: 520px;
    height: 300px;
    background: var(--card);
    border-radius: 26px;
    overflow: hidden;
    box-shadow: 0 14px 30px var(--shadow);
  }
  .card--front { left: 50px; }
  .card--back { left: 630px; }

  /* company name */
  .brand {
    position: absolute;
    color: var(--ink);
    font-family: "Arimo", Arial, sans-serif;
    font-weight: 700;
    text-transform: uppercase;
    letter-spacing: 0.08em;
    white-space: nowrap;
    line-height: 1;
  }
  .card--front .brand {
    left: 0;
    right: 0;
    top: 128px;
    text-align: center;
    font-size: 40px;
  }
  .card--back .brand { left: 40px; top: 106px; font-size: 20px; }

  /* back */
  .person {
    position: absolute;
    right: 40px;
    top: 34px;
    text-align: right;
  }
  .person__name {
    color: var(--ink);
    font-weight: 700;
    font-size: 25px;
    letter-spacing: 0.02em;
    text-transform: uppercase;
  }
  .person__title { color: var(--orange); font-size: 14px; margin-top: 2px; }

  .contacts {
    position: absolute;
    left: 40px;
    top: 186px;
    list-style: none;
    color: var(--ink);
    font-size: 15px;
  }
  .contacts li { display: flex; align-items: center; gap: 12px; height: 26px; }
  .contacts svg { width: 15px; height: 15px; flex: none; }

  .swoosh { position: absolute; inset: 0; width: 100%; height: 100%; }
</style>
</head>
<body>

<section class="card card--front" aria-label="Card front">
  <div class="brand">Velvet Harbor</div>
</section>

<section class="card card--back" aria-label="Card back">
  <svg class="swoosh" viewBox="0 0 520 300" preserveAspectRatio="none" aria-hidden="true">
    <path d="M520 130 C 470 150, 420 230, 300 266 C 240 284, 200 292, 150 300 L520 300 Z" fill="var(--orange-deep)"/>
    <path d="M520 112 C 460 140, 420 210, 300 250 C 240 270, 200 282, 150 292" fill="none" stroke="var(--orange-deep)" stroke-width="2.5"/>
    <path d="M520 122 C 465 146, 420 222, 300 259 C 235 279, 200 288, 150 297" fill="none" stroke="var(--card)" stroke-width="5"/>
  </svg>

  <div class="person">
    <div class="person__name">Nessa Pryle</div>
    <div class="person__title">Founder &amp; Principal</div>
  </div>

  <div class="brand">Velvet Harbor</div>

  <ul class="contacts">
    <li>
      <svg viewBox="0 0 24 24" aria-hidden="true"><path fill="var(--orange)" d="M6.6 10.8a15 15 0 0 0 6.6 6.6l2.2-2.2c.3-.3.7-.4 1-.2 1.1.4 2.3.6 3.6.6.6 0 1 .4 1 1V20c0 .6-.4 1-1 1A17 17 0 0 1 3 4c0-.6.4-1 1-1h3.5c.6 0 1 .4 1 1 0 1.3.2 2.5.6 3.6.1.3 0 .7-.2 1z"/></svg>
      <span>+1.628.309.4156</span>
    </li>
    <li>
      <svg viewBox="0 0 24 24" aria-hidden="true"><rect x="2" y="5" width="20" height="14" rx="2" fill="var(--orange)"/><path d="M3 6l9 7 9-7" fill="none" stroke="var(--card)" stroke-width="1.8"/></svg>
      <span>nessa@velvetharbor.com</span>
    </li>
    <li>
      <svg viewBox="0 0 24 24" aria-hidden="true"><circle cx="12" cy="12" r="9" fill="none" stroke="var(--orange)" stroke-width="2"/><path d="M3 12h18M12 3c3 3 3 15 0 18M12 3c-3 3-3 15 0 18" fill="none" stroke="var(--orange)" stroke-width="1.6"/></svg>
      <span>velvetharbor.com</span>
    </li>
  </ul>
</section>

</body>
</html>
```